Lantern Keepers Lantern Scribes

We would like the business card to be Horizontal
Logo on the back and want it raised.

Target Market(s)

Education and Museums

Industry/Entity Type

Education

Contact Information for Business Card

Dolores Wrenfield, P.H.D.
3918 Pelham Rd
Laurel, MD 20799
612.447.3095
Dolores.Wrenfield@lanternkeeperslanternscribes.org
lanternkeeperslanternscribes.org

Font styles to use
Serif

Colors

Designer to choose colors to be used in the design.

Requirements
Must have
• letters and logo must be raised
• Must be slate blue card
• Silver is aluminum foil

```html
<!DOCTYPE html>
<html lang="en">
<head>
<meta charset="utf-8">
<title>Lantern Keepers Lantern Scribes — Business Card</title>
<link rel="stylesheet" href="https://fonts.googleapis.com/css2?family=Source+Serif+4:wght@400;700&display=swap">
<style>
  :root {
    --backdrop: #ece7df;
    --card-slate: #4b5d7a;
    --card-light: #ffffff;
    --ink: #24304a;
    --ink-soft: #2e3850;
    --mark-raised: #3b4a64;
    --mark-foil: #9aa3ae;
    --band-dark: #26324a;
    --band-mid: #8e98a6;
    --rule: #4b5d7a;
  }
  * { margin: 0; padding: 0; box-sizing: border-box; }
  html, body { width: 1200px; height: 1200px; overflow: hidden; }
  body {
    background: var(--backdrop);
    font-family: "Source Serif 4", serif;
    position: relative;
  }
  .card {
    position: absolute;
    left: 305px;
    width: 585px;
    height: 373px;
    border-radius: 0 40px 0 40px;
    overflow: hidden;
    box-shadow: 0 4px 14px rgba(0,0,0,0.18);
  }
  .card--back { top: 209px; background: var(--card-slate); }
  .card--front { top: 617px; background: var(--card-light); }

  .brand {
    position: absolute;
    display: flex;
    flex-direction: column;
    align-items: center;
    text-align: center;
  }
  .brand__ring {
    border-radius: 50%;
    border: 3px solid currentColor;
  }
  .brand__name {
    font-family: "Source Serif 4", serif;
    font-weight: 700;
    text-transform: uppercase;
    letter-spacing: 0.04em;
    line-height: 1.25;
  }
  .card--back .brand {
    left: 178px; top: 40px; width: 230px;
    color: var(--mark-raised);
  }
  .card--back .brand__ring { width: 110px; height: 110px; margin-bottom: 18px; }
  .card--back .brand__name { font-size: 19px; }

  .card--front .brand {
    left: 38px; top: 60px; width: 200px;
    color: var(--mark-foil);
  }
  .card--front .brand__ring { width: 120px; height: 120px; margin-bottom: 16px; }
  .card--front .brand__name { font-size: 16px; }

  .band {
    position: absolute;
    right: 0;
    clip-path: polygon(0 0, 100% 0, 100% 100%, 5% 100%);
  }
  .card--back .band {
    left: 235px; top: 314px; height: 17px;
    background: linear-gradient(to bottom, var(--band-dark) 55%, var(--band-mid) 55%);
  }
  .card--front .band {
    left: 223px; top: 312px; height: 20px;
    background: linear-gradient(to bottom, var(--band-dark) 45%, var(--band-mid) 45%);
  }

  .divider {
    position: absolute;
    left: 284px; top: 100px;
    width: 12px; height: 80px;
  }

  .contact {
    position: absolute;
    right: 39px; top: 50px;
    text-align: right;
    color: var(--ink-soft);
  }
  .contact__name {
    font-size: 32px;
    font-weight: 400;
    color: var(--ink);
    line-height: 1.1;
    margin-bottom: 4px;
  }
  .contact__line { font-size: 13.5px; line-height: 1.33; }
  .contact__title { margin-bottom: 10px; }

  .online {
    position: absolute;
    left: 245px; top: 264px;
    font-size: 12px;
    line-height: 1.4;
    white-space: nowrap;
    color: var(--ink-soft);
  }
</style>
</head>
<body>

  <section class="card card--back" aria-label="Card back">
    <div class="brand">
      <div class="brand__ring"></div>
      <div class="brand__name">Lantern Keepers<br>Lantern Scribes</div>
    </div>
    <div class="band"></div>
  </section>

  <section class="card card--front" aria-label="Card front">
    <div class="brand">
      <div class="brand__ring"></div>
      <div class="brand__name">Lantern Keepers<br>Lantern Scribes</div>
    </div>

    <svg class="divider" viewBox="0 0 12 80" aria-hidden="true">
      <line x1="2" y1="0" x2="2" y2="80" stroke="var(--rule)" stroke-width="1.5"/>
      <line x1="6" y1="10" x2="6" y2="70" stroke="var(--rule)" stroke-width="1.5"/>
      <line x1="10" y1="0" x2="10" y2="80" stroke="var(--rule)" stroke-width="1.5"/>
    </svg>

    <div class="contact">
      <div class="contact__name">Dolores Wrenfield</div>
      <div class="contact__line contact__title">P.H.D.</div>
      <div class="contact__line">3918 Pelham Rd</div>
      <div class="contact__line">Laurel, MD 20799</div>
      <div class="contact__line">612.447.3095</div>
    </div>

    <div class="online">
      <div>Dolores.Wrenfield@lanternkeeperslanternscribes.org</div>
      <div>lanternkeeperslanternscribes.org</div>
    </div>

    <div class="band"></div>
  </section>

</body>
</html>
```